School Signage

I am wanting designs for signs completed that prompt students of the school requirements for hats, preparation and play.

I've uploaded rough examples of what we're after, but we would like them stylised and better than the example, including:
- A stylised logo/graphic for the 'Wallumba 1, 2, 3'
- Clear, crisp signage for the words.
- Graphics that reinforce the message of the sign.

We're after three signs:
- One that will be located on the oval to prompt hat use.
- One that will be near the entry prompting the morning routine (please make this one landscape with instructions for 'on time' on one side, and 'late' on the other).
- One that will be located within the school prompting readiness for class.

```html
<!DOCTYPE html>
<html lang="en">
<head>
<meta charset="utf-8">
<title>Wallumba 1, 2, 3 – Ready for Class Sign</title>
<link rel="stylesheet" href="https://fonts.googleapis.com/css2?family=Arimo:wght@700&display=swap">
<style>
  :root {
    --sign-yellow: #f9e816;
    --sign-green: #1c3b22;
    --text-white: #ffffff;
    --phone-light: #c9ccc8;
    --phone-mid: #a9ada8;
    --phone-dark: #7d827c;
    --page-bg: #ececec;
  }
  html, body {
    margin: 0;
    padding: 0;
    width: 1200px;
    height: 1200px;
    overflow: hidden;
    background: var(--page-bg);
    font-family: "Arimo", Arial, sans-serif;
    font-weight: 700;
  }
  .sign {
    position: absolute;
    left: 40px;
    top: 251px;
    width: 1120px;
    height: 697px;
    overflow: hidden;
    background: var(--sign-yellow);
  }
  .sign-backdrop {
    position: absolute;
    inset: 0;
  }
  .school-name {
    position: absolute;
    left: 67px;
    top: 92px;
    width: 200px;
    display: flex;
    align-items: center;
    gap: 12px;
    color: var(--sign-green);
    font-size: 26px;
    line-height: 1.15;
  }
  .school-name-dot {
    flex: none;
    width: 22px;
    height: 22px;
    border-radius: 50%;
    background: var(--sign-green);
  }
  .sign-heading {
    position: absolute;
    right: 83px;
    top: 78px;
    margin: 0;
    text-align: right;
    color: var(--sign-green);
    line-height: 1;
  }
  .sign-title {
    display: block;
    font-size: 59px;
    letter-spacing: -0.3px;
  }
  .sign-subtitle {
    display: block;
    margin-top: 24px;
    font-size: 46px;
  }
  .checklist {
    position: absolute;
    left: 97px;
    top: 338px;
    margin: 0;
    padding: 0;
    list-style: none;
    color: var(--sign-yellow);
    font-size: 32px;
    line-height: 1.3;
  }
  .checklist-item {
    position: absolute;
    left: 0;
    display: flex;
    align-items: center;
    white-space: nowrap;
  }
  .checklist-item:nth-child(1) { top: 0; }
  .checklist-item:nth-child(2) { top: 113px; }
  .checklist-item:nth-child(3) { top: 220px; }
  .checklist-icon {
    flex: none;
    width: 88px;
    height: 88px;
    margin-right: 32px;
  }
  .values {
    position: absolute;
    right: 83px;
    top: 524px;
    text-align: right;
  }
  .values-name {
    display: block;
    color: var(--text-white);
    font-size: 33px;
  }
  .values-label {
    display: block;
    margin-top: 4px;
    color: var(--sign-yellow);
    font-size: 19.5px;
  }
</style>
</head>
<body>
  <main class="sign">
    <svg class="sign-backdrop" width="1120" height="697" viewBox="0 0 1120 697" role="img" aria-label="Green wave band where the decorative dotted and flowing line motif sits">
      <path fill="var(--sign-green)" d="M0,295 C90,270 200,250 315,255 C520,262 760,335 960,330 C1030,328 1080,318 1120,310 L1120,697 L0,697 Z"/>
    </svg>

    <div class="school-name">
      <span class="school-name-dot"></span>
      <span>Wallumba State High</span>
    </div>

    <h1 class="sign-heading">
      <span class="sign-title">Are you ready for class?</span>
      <span class="sign-subtitle">The Wallumba 1, 2, 3</span>
    </h1>

    <ol class="checklist">
      <li class="checklist-item">
        <svg class="checklist-icon" viewBox="0 0 88 88" aria-hidden="true">
          <circle cx="44" cy="44" r="41" fill="none" stroke="var(--sign-yellow)" stroke-width="3"/>
          <rect x="28" y="30" width="32" height="22" rx="1.5" fill="none" stroke="var(--sign-yellow)" stroke-width="2.5"/>
          <path d="M22,57 H66 L63,61 H25 Z" fill="var(--sign-yellow)"/>
        </svg>
        <span>1. Laptop/workbook</span>
      </li>
      <li class="checklist-item">
        <svg class="checklist-icon" viewBox="0 0 88 88" aria-hidden="true">
          <circle cx="44" cy="44" r="41" fill="none" stroke="var(--sign-yellow)" stroke-width="3"/>
          <ellipse cx="36" cy="54" rx="13" ry="7" fill="var(--phone-light)"/>
          <rect x="42" y="26" width="18" height="34" rx="4" transform="rotate(-20 51 43)" fill="var(--phone-mid)"/>
          <rect x="46" y="31" width="10" height="20" rx="1.5" transform="rotate(-20 51 43)" fill="var(--phone-dark)"/>
        </svg>
        <span>2. Phone in Pouchlock</span>
      </li>
      <li class="checklist-item">
        <svg class="checklist-icon" viewBox="0 0 88 88" aria-hidden="true">
          <circle cx="44" cy="44" r="41" fill="none" stroke="var(--sign-yellow)" stroke-width="3"/>
          <path d="M24,52 C24,36 34,28 46,28 C58,28 64,38 64,50 Z" fill="none" stroke="var(--sign-yellow)" stroke-width="2.5" stroke-linejoin="round"/>
          <path d="M22,53 C30,58 46,60 66,52 C62,60 44,64 26,58 Z" fill="none" stroke="var(--sign-yellow)" stroke-width="2.5" stroke-linejoin="round"/>
          <rect x="49" y="35" width="8" height="9" rx="1" fill="var(--sign-yellow)"/>
        </svg>
        <span>3. Correct uniform<br>(including hat)</span>
      </li>
    </ol>

    <div class="values">
      <span class="values-name">Curiosity and Drive</span>
      <span class="values-label">Wallumba Learner Values</span>
    </div>
  </main>
</body>
</html>
```